CareWillow Brand Standards and Core Values

I would like to have frameable posters made up for each office using our brand standards. I would like the posters to include:Our Vision Statement:We are transforming the healthcare staffing and homecare industry with our people-oriented, world-class team. Clients choose us, and develop lasting bonds with our team because of our impeccably high standards and our reputation for always remembering this is, first and foremost, a people business. We consistently go the extra mile to ensure our nurses and those being cared for are at all times, treated with dignity and respect. We hold ourselves and those we work with to the highest possible standards. We consistently deliver what we promise, and whenever possible, even more. Our Mission Statement:We go above and beyond to ensure our clients receive the right care and the right people at the right time. Our rigorous recruitment standards result in strong caregivers who are trusted for their expertise, experience and compassion. Our Values:Through our genuine caring and compassion, we are committed to honor all with whom we interact. We are grounded in our faith and dedicated to working together as a family that consistently and passionately lives our values. Compassion Integrity and honesty Faith Decisive action Constant and never-ending improvement Personal ownership Excellence Positive attitude Passion RespectWho we are:We are friendly, servant leaders who have a sense of urgency to meet the needs of our nurses and clients. We prioritize personal relationships with genuine caring and compassion. We inspire others through our passion and energy.Our main colors are: HEX# 5C80DE, HEX# BDE080, HEX# 8C8C8Caccent colors are: HEX# 95D6E3, HEX# AD59AB, HEX# 002E57

Target Market(s)

office employee inspiration

Font styles to use
Other font styles liked:
• Verdana

Colors

Designer to choose colors to be used in the design.

Requirements
Must have
• the core values listed in description
Nice to have
• colors given in description, something fun and inspiring for office employees to help motivate them !
Should not have
• colors that are not company colors. I have listed HEX codes in description

```html
<!DOCTYPE html>
<html lang="en">
<head>
<meta charset="utf-8">
<title>CareWillow – Our Vision</title>
<link href="https://fonts.googleapis.com/css2?family=Oswald:wght@700&family=Montserrat:wght@800&family=Lato:wght@400&display=swap" rel="stylesheet">
<style>
  :root{
    --navy:#17325e;
    --board:#2d2d2d;
    --grey-text:#7a7a7a;
    --brand-blue:#5c80de;
    --red-a:#8e1a24; --red-b:#e0303f;
    --amber-a:#9c6628; --amber-b:#f2a321;
    --sky-a:#1565a0; --sky-b:#28a8de;
    --plum-a:#4a0a30; --plum-b:#8c1c5c;
    --page:#ffffff;
    --backdrop:#e6e6e6;
  }
  *{margin:0;padding:0;box-sizing:border-box}
  html,body{width:1200px;height:1200px;overflow:hidden;background:var(--backdrop)}
  .poster{
    position:absolute;left:190px;top:20px;width:940px;height:1330px;
    background:var(--page);transform:scale(0.8722);transform-origin:top left;
    overflow:hidden;
  }
  .title{
    position:absolute;left:100px;top:62px;
    font-family:"Oswald",sans-serif;font-weight:700;font-size:104px;line-height:1.1;
    color:var(--navy);letter-spacing:-1px;
  }
  .brand{
    position:absolute;left:585px;top:92px;display:flex;align-items:center;gap:14px;
  }
  .brand-dot{width:34px;height:34px;border-radius:50%;background:var(--brand-blue)}
  .brand-name{font-family:"Lato",sans-serif;font-size:30px;color:var(--grey-text)}
  .board-svg{position:absolute;left:0;top:0}
  .frame{
    position:absolute;left:162px;width:590px;height:172px;border-radius:18px;
    background:var(--page);
    box-shadow:0 0 0 1px #e4e4e4, inset 0 0 10px rgba(0,0,0,.10), 0 3px 6px rgba(0,0,0,.08);
  }
  .value-card{
    position:absolute;left:186px;width:544px;height:130px;border-radius:16px;
    color:#fff;padding:14px 120px 0 25px;
    box-shadow:8px 10px 14px rgba(0,0,0,.45);
  }
  .value-card h2{
    font-family:"Montserrat",sans-serif;font-weight:800;font-size:22px;letter-spacing:.5px;
    text-transform:uppercase;margin-bottom:6px;
  }
  .value-card p{font-family:"Lato",sans-serif;line-height:1.3}
  .card-red{top:383px;background:radial-gradient(ellipse at 55% 30%,var(--red-b),var(--red-a) 75%)}
  .card-red p{font-size:17px}
  .card-amber{top:573px;background:radial-gradient(ellipse at 55% 30%,var(--amber-b),var(--amber-a) 75%)}
  .card-amber p{font-size:14.5px}
  .card-sky{top:761px;background:radial-gradient(ellipse at 45% 35%,var(--sky-b),var(--sky-a) 75%)}
  .card-sky h2{margin-top:10px;margin-bottom:10px}
  .card-sky p{font-size:15.5px;padding-right:0;width:430px}
  .card-plum{top:946px;background:radial-gradient(ellipse at 40% 20%,var(--plum-b),var(--plum-a) 75%)}
  .card-plum p{font-size:15.5px}
  .card-icon{position:absolute;right:24px;top:32px;width:70px;height:70px}
  .footer{
    position:absolute;left:0;bottom:0;width:100%;height:84px;background:var(--navy);
    display:flex;align-items:center;justify-content:center;
    font-family:"Oswald",sans-serif;font-weight:700;font-size:34px;color:#fff;
  }
</style>
</head>
<body>
<main class="poster">
  <h1 class="title">OUR VISION</h1>
  <div class="brand"><span class="brand-dot"></span><span class="brand-name">CareWillow</span></div>

  <svg class="board-svg" width="940" height="1330" viewBox="0 0 940 1330" aria-hidden="true">
    <path class="board-clip" d="M328 228 Q460 185 590 228 L590 283 Q460 270 328 283 Z" fill="var(--board)"/>
    <path class="board-top" d="M166 330 Q166 305 190 303 Q460 282 730 303 Q752 306 752 330 L752 352 L166 352 Z" fill="var(--board)"/>
    <path class="board-bottom" d="M161 1118 L747 1118 L747 1150 Q747 1165 725 1167 Q460 1190 185 1167 Q161 1165 161 1150 Z" fill="var(--board)"/>
  </svg>

  <div class="frame" style="top:365px"></div>
  <div class="frame" style="top:555px"></div>
  <div class="frame" style="top:745px"></div>
  <div class="frame" style="top:930px"></div>

  <section class="value-card card-red">
    <h2>Transforming</h2>
    <p>We are transforming the healthcare staffing and homecare industry with our people-oriented, world-class team.</p>
    <svg class="card-icon" viewBox="0 0 70 70" aria-hidden="true">
      <path d="M35 62 L8 34 A16 16 0 0 1 35 12 A16 16 0 0 1 62 34 Z" fill="#fff"/>
      <polyline points="6,38 22,38 27,30 33,46 39,26 44,38 64,38" fill="none" stroke="#c8202f" stroke-width="3.5" stroke-linejoin="round"/>
    </svg>
  </section>

  <section class="value-card card-amber">
    <h2>Choose Us</h2>
    <p>Clients choose us, and develop lasting bonds with our team because of our impeccably high standards and our reputation for always remembering this is, first and foremost, a people business.</p>
    <svg class="card-icon" viewBox="0 0 70 70" aria-hidden="true">
      <rect x="25" y="8" width="20" height="10" rx="3" fill="none" stroke="#fff" stroke-width="4"/>
      <rect x="5" y="17" width="60" height="44" rx="5" fill="#fff"/>
      <path d="M5 34 H65" stroke="#c88424" stroke-width="2.5"/>
      <rect x="29" y="30" width="12" height="9" rx="2" fill="#fff" stroke="#c88424" stroke-width="2.5"/>
    </svg>
  </section>

  <section class="value-card card-sky">
    <h2>Consistency</h2>
    <p>We consistently go the extra mile to ensure our nurses and those being cared for are at all times, treated with dignity and respect.</p>
    <svg class="card-icon" viewBox="0 0 70 70" aria-hidden="true">
      <circle cx="35" cy="38" r="22" fill="none" stroke="#fff" stroke-width="5"/>
      <path d="M35 26 V39 H45" fill="none" stroke="#fff" stroke-width="4"/>
      <path d="M8 18 A10 10 0 0 1 22 8 Z M62 18 A10 10 0 0 0 48 8 Z" fill="#fff"/>
      <path d="M18 58 L12 66 M52 58 L58 66" stroke="#fff" stroke-width="5" stroke-linecap="round"/>
    </svg>
  </section>

  <section class="value-card card-plum">
    <h2>High Standards</h2>
    <p>We hold ourselves and those we work with to the highest possible standards. We consistently deliver what we promise, and whenever possible, even more.</p>
    <svg class="card-icon" viewBox="0 0 70 70" aria-hidden="true">
      <path d="M4 2 V66 H66" fill="none" stroke="#fff" stroke-width="3"/>
      <path d="M12 60 V44 L24 34 V60 Z M28 60 V36 L38 44 V60 Z M42 60 V40 L56 26 V60 Z" fill="#fff"/>
      <polyline points="10,38 24,26 38,36 58,14" fill="none" stroke="#fff" stroke-width="3.5"/>
      <path d="M50 10 H62 V22 Z" fill="#fff"/>
    </svg>
  </section>

  <footer class="footer">www.yourwebsite.com</footer>
</main>
</body>
</html>
```